Design some Business Cards for Quizwell

I would like to have a business card designed.

Use the logo from https://www.quizwell-demo.net - we're an education company, keep it elegant and simple; nothing too extravagant. Double Sided isn't necessary but could be better.

Name: Dov Renkel, Founder
Email: dov@quizwell-demo.net
Phone: 5550142986
website: https://www.quizwell-demo.net

Would like the slogan "Testing Made Simple and Clear" on the back if possible.

```html
<!DOCTYPE html>
<html lang="en">
<head>
<meta charset="utf-8">
<title>Quizwell Business Card</title>
<link href="https://fonts.googleapis.com/css2?family=Questrial&family=Montserrat:wght@600;700&display=swap" rel="stylesheet">
<style>
  :root {
    --page: #e9e8e6;
    --card-dark: #151515;
    --card-light: #ffffff;
    --ink: #1a1a1a;
    --ink-soft: #4a4a4a;
    --green: #7dc242;
  }
  * { box-sizing: border-box; margin: 0; padding: 0; }
  html, body {
    width: 1200px; height: 811px; overflow: hidden;
    background: var(--page);
    font-family: "Questrial", sans-serif;
  }
  .stage {
    width: 1200px; height: 811px;
    display: flex; flex-direction: column; align-items: center; justify-content: center;
    gap: 48px;
  }
  .card {
    position: relative; width: 620px; height: 354px; overflow: hidden;
    border-radius: 4px;
    box-shadow: 0 10px 28px rgba(0,0,0,.18);
  }
  .brand { position: absolute; display: flex; align-items: center; gap: 14px; }
  .brand__dot { width: 18px; height: 18px; border-radius: 50%; background: var(--green); flex: none; }
  .brand__name { font-family: "Questrial", sans-serif; font-size: 76px; line-height: 1; letter-spacing: 1px; }

  /* back side */
  .card--back { background: var(--card-dark); }
  .card--back .brand { left: 62px; top: 112px; }
  .card--back .brand__name { color: #ffffff; }
  .slogan {
    position: absolute; left: 96px; top: 198px;
    color: var(--green); font-size: 24px; letter-spacing: .5px;
  }

  /* front side */
  .card--front { background: var(--card-light); }
  .card--front .brand { left: 34px; top: 128px; }
  .card--front .brand__name { color: var(--ink); font-size: 72px; }
  .contact { position: absolute; left: 392px; top: 104px; }
  .contact__head { padding-left: 14px; border-left: 3px solid var(--green); }
  .contact__name {
    font-family: "Montserrat", sans-serif; font-weight: 700;
    color: var(--green); font-size: 17px; letter-spacing: .5px; text-transform: uppercase; line-height: 1.2;
  }
  .contact__role {
    font-family: "Montserrat", sans-serif; font-weight: 600;
    color: var(--ink); font-size: 11px; margin-top: 2px;
  }
  .contact__list { list-style: none; margin-top: 14px; }
  .contact__item {
    display: flex; align-items: center; gap: 9px;
    font-size: 14px; color: var(--ink-soft); line-height: 1; margin-bottom: 10px;
  }
  .contact__item svg { width: 12px; height: 12px; flex: none; }
</style>
</head>
<body>
<main class="stage">
  <section class="card card--back" aria-label="Card back">
    <div class="brand">
      <span class="brand__dot"></span>
      <span class="brand__name">Quizwell</span>
    </div>
    <p class="slogan">Testing Made Simple and Clear</p>
  </section>

  <section class="card card--front" aria-label="Card front">
    <div class="brand">
      <span class="brand__dot"></span>
      <span class="brand__name">Quizwell</span>
    </div>
    <div class="contact">
      <div class="contact__head">
        <p class="contact__name">Dov Renkel</p>
        <p class="contact__role">Founder</p>
      </div>
      <ul class="contact__list">
        <li class="contact__item">
          <svg viewBox="0 0 24 24" aria-hidden="true"><path fill="#7dc242" d="M6.6 10.8a15.1 15.1 0 0 0 6.6 6.6l2.2-2.2a1 1 0 0 1 1-.25 11.4 11.4 0 0 0 3.6.57 1 1 0 0 1 1 1V20a1 1 0 0 1-1 1A17 17 0 0 1 3 4a1 1 0 0 1 1-1h3.5a1 1 0 0 1 1 1c0 1.25.2 2.45.57 3.57a1 1 0 0 1-.25 1z"/></svg>
          5550142986
        </li>
        <li class="contact__item">
          <svg viewBox="0 0 24 24" aria-hidden="true"><rect x="2" y="5" width="20" height="14" fill="#7dc242"/><path d="M2 5l10 8 10-8" fill="none" stroke="#ffffff" stroke-width="2"/></svg>
          dov@quizwell-demo.net
        </li>
        <li class="contact__item">
          <svg viewBox="0 0 24 24" aria-hidden="true"><circle cx="12" cy="12" r="10" fill="none" stroke="#7dc242" stroke-width="2.4"/><path d="M2 12h20M12 2c3 3 3 17 0 20M12 2c-3 3-3 17 0 20" fill="none" stroke="#7dc242" stroke-width="2"/></svg>
          www.quizwell-demo.net
        </li>
      </ul>
    </div>
  </section>
</main>
</body>
</html>
```